Yard sign design for high end luxury home builder.

Need a design for signage on custom homes that are being built. I already have a logo that I am satisfied with that needs to be incorporated. I need the following incorporated in the design of the sign-
- Lic number 582316
- phone number (805) 471-2938‬
- tembleyhomeworks.com
- Logo/Branding

If possible it may be nice to have the following quote that is on are business cards-

Quote from Corwin of Valdema-
HE WHO WORKS WITH HIS HANDS IS A LABORER.
HE WHO WORKS WITH HIS HANDS & HIS HEAD IS A CRAFTSMAN.
HE WHO WORKS WITH HIS HANDS & HIS HEAD & HIS HEART IS AN ARTISAN.
-CORWIN OF VALDEMA

Target Market(s)

Archetect, Designers, Clients desiring to build a new home or remodel.

Colors
fde9d4
fee4d5
fabb94
fac994
faa54b
f68d4d
f37122
f78f20
f68e4e

Requirements
Must have
• - Lic number 582316
• - phone number (805) 471-2938‬
• - tembleyhomeworks.com
• - Logo/Branding
Nice to have
• Quote from Corwin of Valdema-
• HE WHO WORKS WITH HIS HANDS IS A LABORER.
• HE WHO WORKS WITH HIS HANDS & HIS HEAD IS A CRAFTSMAN.
• HE WHO WORKS WITH HIS HANDS & HIS HEAD & HIS HEART IS AN ARTISAN.
• -CORWIN OF VALDEMA
• OR the below statement-
• Craftsmen that Care
Should not have
• Any additional verbiage not specified above including any type of verbiage about what kind of company we are. For instance- Integrity, reputable... It's just all played out. Im just looking for a bitching design that has the info that compliments my logo/branding.

```html
<!DOCTYPE html>
<html lang="en">
<head>
<meta charset="utf-8">
<title>Tembley Homeworks – Yard Sign</title>
<link rel="stylesheet" href="https://fonts.googleapis.com/css2?family=Saira:ital,wght@0,500;0,600;0,700;1,700&display=swap">
<style>
  :root {
    --canvas-bg: #ebe8e4;
    --peach: #fcca98;
    --stucco: #ebe5dd;
    --band-orange: #f78f20;
    --stripe-dark: #f37122;
    --stripe-light: #faa54b;
    --fold-shade: #c9661a;
    --ink: #1d1b1a;
    --brand-grey: #706861;
    --brand-block: #7d6b5b;
    --lic-grey: #8b7b6c;
  }
  html, body {
    margin: 0;
    padding: 0;
    width: 1200px;
    height: 800px;
    overflow: hidden;
    background: var(--canvas-bg);
  }
  .yard-sign {
    position: absolute;
    left: 40px;
    top: 151px;
    width: 1120px;
    height: 497px;
    display: block;
    box-shadow: 0 6px 18px rgba(0,0,0,0.18);
  }
  .sign-text { font-family: "Saira", sans-serif; }
  .phone { font-weight: 700; font-size: 38px; fill: var(--ink); letter-spacing: 0.5px; }
  .website { font-weight: 700; font-size: 30px; fill: var(--ink); }
  .quote-line { font-weight: 700; font-style: italic; font-size: 18px; fill: var(--ink); letter-spacing: 0.9px; }
  .quote-author { font-weight: 700; font-style: italic; font-size: 18px; fill: var(--ink); letter-spacing: 0.9px; }
  .brand-name { font-weight: 700; font-size: 27px; fill: var(--brand-grey); letter-spacing: 1.5px; }
  .lic-label { font-weight: 600; font-size: 19px; fill: var(--lic-grey); }
  .lic-number { font-weight: 700; font-size: 23px; fill: var(--lic-grey); letter-spacing: 1px; }
  .icon-line { fill: none; stroke: var(--ink); stroke-width: 2; }
</style>
</head>
<body>
<svg class="yard-sign" viewBox="0 0 824 366" xmlns="http://www.w3.org/2000/svg" role="img" aria-label="Tembley Homeworks yard sign">
  <!-- base panels -->
  <rect class="panel-peach" x="0" y="0" width="824" height="366" fill="var(--peach)"/>
  <polygon class="panel-stucco" points="505,0 824,0 824,366 270,366" fill="var(--stucco)"/>

  <!-- diagonal accent stripes -->
  <polygon class="stripe-dark" points="410,0 440,0 200,366 170,366" fill="var(--stripe-dark)"/>
  <polygon class="stripe-light" points="440,0 505,0 270,366 200,366" fill="var(--stripe-light)"/>

  <!-- contact band -->
  <polygon class="band-fold" points="296,141 345,141 318,162" fill="var(--fold-shade)"/>
  <polygon class="contact-band" points="354,30 824,30 824,141 281,141" fill="var(--band-orange)"/>

  <!-- phone icon -->
  <g class="icon-phone" transform="translate(364,68)">
    <circle class="icon-line" cx="0" cy="0" r="10"/>
    <path d="M-4.5,-5.5 l2.5,-1 l2,3.5 l-1.8,1.5 q1.2,2.8 3.8,4 l1.5,-1.8 l3.5,2 l-1,2.5 q-7,0.5 -10.5,-10.7z" fill="var(--ink)"/>
  </g>
  <text class="sign-text phone" x="804" y="82" text-anchor="end">(805) 471-2938</text>

  <!-- globe icon -->
  <g class="icon-globe" transform="translate(341,106)">
    <circle class="icon-line" cx="0" cy="0" r="10"/>
    <ellipse class="icon-line" cx="0" cy="0" rx="4.5" ry="10"/>
    <line class="icon-line" x1="-10" y1="0" x2="10" y2="0"/>
    <line class="icon-line" x1="-8.5" y1="-5" x2="8.5" y2="-5"/>
    <line class="icon-line" x1="-8.5" y1="5" x2="8.5" y2="5"/>
  </g>
  <text class="sign-text website" x="804" y="117" text-anchor="end">tembleyhomeworks.com</text>

  <!-- quote -->
  <g class="quote">
    <text class="sign-text quote-line" x="436" y="185">HE WHO WORKS WITH HIS HANDS</text>
    <text class="sign-text quote-line" x="421" y="211">IS A LABORER.</text>
    <text class="sign-text quote-line" x="407" y="238">HE WHO WORKS WITH HIS HANDS</text>
    <text class="sign-text quote-line" x="386" y="264">&amp; HIS HEAD IS A CRAFTSMAN.</text>
    <text class="sign-text quote-line" x="372" y="291">HE WHO WORKS WITH HIS HANDS</text>
    <text class="sign-text quote-line" x="351" y="317">&amp; HIS HEAD &amp; HIS HEART IS AN ARTISAN.</text>
    <text class="sign-text quote-author" x="796" y="345" text-anchor="end">CORWIN OF VALDEMA</text>
  </g>

  <!-- brand block -->
  <g class="brand">
    <rect class="brand-square" x="32" y="30" width="150" height="150" fill="var(--brand-block)"/>
    <text class="sign-text brand-name" x="32" y="218">TEMBLEY</text>
    <text class="sign-text brand-name" x="32" y="248">HOMEWORKS</text>
  </g>

  <!-- license -->
  <text class="sign-text lic-label" x="32" y="311">Lic number</text>
  <text class="sign-text lic-number" x="32" y="340">582316</text>
</svg>
</body>
</html>
```